Halvorn Homes-Real Estate of the Future

Halvorn Homes is a Residential Real Estate company which specializes in buying and selling homes. We pride ourselves on service, expertise, and building relationships. I would like to do a Billboard Ad for a The Size is 14 feet (Height) x 48 feet (width) displaying our current motto for "Real Estate of the Future" We have launched new programs and working with leaders in our industy Brimlot and other tech companies and changing the way Real Estate is done in Las Vegas, NV. Its exciting and NEW so we want to get the word out. Color Scheme Red, White, Grey and maybe black. Logo is uploaded and so is a picture head shot. I would like to see options with my headshot and with out.

```html
<!DOCTYPE html>
<html lang="en">
<head>
<meta charset="utf-8">
<title>Halvorn Homes – Real Estate of the Future Billboard</title>
<link href="https://fonts.googleapis.com/css2?family=Marcellus&display=swap" rel="stylesheet">
<style>
  :root {
    --page-bg: #f3f3f3;
    --brand-red: #c01e26;
    --ink-black: #111111;
    --swoosh-grey: #3a3a3c;
    --swoosh-silver: #d6d6d8;
    --white: #ffffff;
  }
  * { margin: 0; padding: 0; box-sizing: border-box; }
  html, body {
    width: 1200px; height: 831px; overflow: hidden;
    background: var(--page-bg);
    font-family: "Marcellus", "Times New Roman", serif;
  }
  .stage { position: relative; width: 1200px; height: 831px; }

  .billboard {
    position: absolute;
    width: 1200px; height: 349px;
    overflow: hidden;
    background: var(--white);
  }
  .billboard--preview {
    left: 79px; top: 88px;
    transform: scale(0.8683);
    transform-origin: top left;
    box-shadow: 0 34px 30px -24px rgba(0,0,0,0.35);
  }
  .billboard--full { left: 0; top: 482px; }

  .billboard__photo {
    position: absolute; left: 0; top: 0; width: 100%; height: 100%;
    background:
      linear-gradient(90deg, #ffffff 0%, #ffffff 22%, rgba(255,255,255,0.75) 34%, rgba(255,255,255,0) 52%),
      radial-gradient(ellipse at 96% 5%, #3c4a2c 0%, rgba(60,74,44,0) 30%),
      linear-gradient(180deg, rgba(0,0,0,0) 55%, rgba(40,38,46,0.35) 100%),
      linear-gradient(90deg, #e4dde2 30%, #b7a8b4 50%, #8c7c8b 65%, #6d6170 80%, #4b4650 100%);
  }

  .billboard__shapes { position: absolute; left: 0; top: 0; width: 100%; height: 100%; }

  .brand-name {
    position: absolute; left: 58px; top: 132px;
    font-size: 46px; letter-spacing: 1px;
    color: var(--brand-red);
    text-transform: uppercase;
    white-space: nowrap;
  }
  .motto {
    position: absolute; left: 100px; top: 230px; width: 345px;
    text-align: center; text-transform: uppercase; line-height: 1;
  }
  .motto__lead { display: block; font-size: 45px; color: var(--brand-red); }
  .motto__tail { display: block; font-size: 36px; color: var(--ink-black); margin-top: 10px; }

  .values {
    position: absolute; right: 36px; top: 96px;
    text-align: right; text-transform: uppercase; color: var(--white);
    line-height: 1;
  }
  .values__intro { display: block; font-size: 31px; }
  .values__highlight {
    display: inline-block; margin-top: 8px;
    background: var(--brand-red);
    font-size: 44px; padding: 4px 6px 4px 10px;
  }
  .values__detail { display: block; font-size: 27px; margin-top: 6px; line-height: 1.15; }
</style>
</head>
<body>
<main class="stage">

  <section class="billboard billboard--preview">
    <div class="billboard__photo" role="img" aria-label="Headshot of the agent in a navy blazer and blue shirt, set before a softly blurred row of suburban homes"></div>
    <svg class="billboard__shapes" viewBox="0 0 1200 349" preserveAspectRatio="none" aria-hidden="true">
      <path d="M20 0 H655 C520 55 400 74 300 72 C180 70 90 40 20 0 Z" fill="var(--brand-red)"/>
      <path d="M0 6 C100 62 200 86 300 86 C430 86 560 50 662 0" fill="none" stroke="var(--swoosh-silver)" stroke-width="9"/>
      <path d="M0 10 C100 68 200 94 300 94 C432 94 565 54 668 0" fill="none" stroke="var(--swoosh-grey)" stroke-width="8"/>
      <path d="M660 349 C760 300 860 282 960 285 C1060 288 1140 312 1200 338 V349 Z" fill="var(--brand-red)"/>
      <path d="M610 349 C720 295 830 272 950 275 C1060 278 1140 302 1200 330" fill="none" stroke="var(--white)" stroke-width="7"/>
    </svg>
    <div class="brand-name">Halvorn Homes</div>
    <h1 class="motto"><span class="motto__lead">Real Estate</span><span class="motto__tail">of the Future</span></h1>
    <div class="values">
      <span class="values__intro">We pride ourselves</span>
      <span class="values__highlight">On Service</span>
      <span class="values__detail">Expertise &amp; Building<br>Relationships</span>
    </div>
  </section>

  <section class="billboard billboard--full">
    <div class="billboard__photo" role="img" aria-label="Headshot of the agent in a navy blazer and blue shirt, set before a softly blurred row of suburban homes"></div>
    <svg class="billboard__shapes" viewBox="0 0 1200 349" preserveAspectRatio="none" aria-hidden="true">
      <path d="M20 0 H655 C520 55 400 74 300 72 C180 70 90 40 20 0 Z" fill="var(--brand-red)"/>
      <path d="M0 6 C100 62 200 86 300 86 C430 86 560 50 662 0" fill="none" stroke="var(--swoosh-silver)" stroke-width="9"/>
      <path d="M0 10 C100 68 200 94 300 94 C432 94 565 54 668 0" fill="none" stroke="var(--swoosh-grey)" stroke-width="8"/>
      <path d="M660 349 C760 300 860 282 960 285 C1060 288 1140 312 1200 338 V349 Z" fill="var(--brand-red)"/>
      <path d="M610 349 C720 295 830 272 950 275 C1060 278 1140 302 1200 330" fill="none" stroke="var(--white)" stroke-width="7"/>
    </svg>
    <div class="brand-name">Halvorn Homes</div>
    <h2 class="motto"><span class="motto__lead">Real Estate</span><span class="motto__tail">of the Future</span></h2>
    <div class="values">
      <span class="values__intro">We pride ourselves</span>
      <span class="values__highlight">On Service</span>
      <span class="values__detail">Expertise &amp; Building<br>Relationships</span>
    </div>
  </section>

</main>
</body>
</html>
```